business card for WRT pty ltd

We require a business card that stands out . I have included our company flyer and would like the services listed to be put on the card so when we Give out the cards to customers they have an idea of services we provide. need the winning design to be in editable photo shop format, editable iMac pages format or editable windows publisher format, so that I can enter in names, email addresses, phone numbers etc myself. I have included a pdf documents of info / items needed on the card to use as reference please.
Updates

need more submissions

Need extra days to review

Sick

Target Market(s)

new customers

Contact Information for Business Card

details are on attached business card requirements file

Requirements
Must have
• I have attached a list of must haves

```html
<!DOCTYPE html>
<html lang="en">
<head>
<meta charset="utf-8">
<title>WRT Pty Ltd – Business Card</title>
<link rel="stylesheet" href="https://fonts.googleapis.com/css2?family=Roboto+Condensed:wght@300;400;700&family=Roboto:wght@700&display=swap">
<style>
  :root {
    --page: #e4e4e4;
    --card: #0d0d0e;
    --card-mid: #1b1b1d;
    --gold: #d9b064;
    --amber: #b8742a;
    --silver: #b9bcc0;
    --white: #f4f4f4;
    --desert: #b5693a;
    --desert-light: #d59a66;
  }
  * { margin: 0; padding: 0; box-sizing: border-box; }
  html, body { width: 1200px; height: 1200px; overflow: hidden; }
  body {
    background: var(--page);
    font-family: "Roboto Condensed", "Arial Narrow", sans-serif;
    position: relative;
  }
  .card {
    position: absolute;
    left: 150px;
    width: 900px;
    height: 514px;
    border-radius: 26px;
    overflow: hidden;
    background: radial-gradient(ellipse at 60% 35%, var(--card-mid) 0%, var(--card) 70%);
    box-shadow: 0 10px 24px rgba(0,0,0,0.28);
  }
  .card-front { top: 56px; }
  .card-back { top: 630px; }

  .brand-name {
    position: absolute;
    font-family: "Roboto Condensed", sans-serif;
    font-weight: 700;
    color: var(--silver);
    letter-spacing: 4px;
    line-height: 1;
  }
  .card-front .brand-name {
    top: 36px; left: 0; width: 100%;
    text-align: center;
    font-size: 118px;
  }
  .services {
    position: absolute;
    top: 190px; left: 0; width: 100%;
    text-align: center;
    color: var(--gold);
    font-weight: 300;
    font-size: 21px;
    line-height: 26px;
  }
  .services .dot { margin: 0 6px; font-size: 14px; vertical-align: 2px; }
  .fleet-photo {
    position: absolute;
    left: 0; bottom: 0;
    width: 100%; height: 236px;
    background: linear-gradient(180deg, rgba(13,13,14,0) 0%, #3a2a20 28%, var(--desert) 62%, var(--desert-light) 100%);
  }

  .truck-photo {
    position: absolute;
    left: 0; top: 30px;
    width: 460px; height: 484px;
    background: linear-gradient(120deg, #1e1e20 0%, #2b2622 45%, #6b5638 80%, rgba(13,13,14,0) 100%);
    border-top-right-radius: 60px;
  }
  .card-back .brand-name {
    top: 64px; right: 50px;
    font-size: 96px;
  }
  .contact {
    position: absolute;
    right: 54px; top: 194px;
    text-align: right;
    color: var(--white);
    font-size: 21px;
    line-height: 26px;
  }
  .person-name {
    font-family: "Roboto", sans-serif;
    font-weight: 700;
    color: var(--amber);
    font-size: 30px;
    line-height: 34px;
    letter-spacing: 0.5px;
  }
  .company { color: var(--amber); font-weight: 700; margin-top: 16px; }
  .lines { margin-top: 22px; }
  .line { display: flex; justify-content: flex-end; align-items: center; gap: 10px; }
  .line svg { width: 16px; height: 16px; flex: none; }
</style>
</head>
<body>

<section class="card card-front">
  <div class="brand-name">WRT</div>
  <p class="services">
    Over size loads / Hot Shot Loads<span class="dot">●</span>Heavy Vehicle Recovery services<span class="dot">●</span>Potable Water Deliveries<br>
    Road Building / Maintenance<span class="dot">●</span>Earthworks<span class="dot">●</span>Sand &amp; Metal Supply &amp; Cartage<br>
    Road Train Tippers<span class="dot">●</span>Road Train Tankers<span class="dot">●</span>Road Train Flat Tops<span class="dot">●</span>Drop Deck Trailers<br>
    Mine site accredited equipment &amp; Operators
  </p>
  <div class="fleet-photo" role="img" aria-label="Photo of a road train truck hauling tipper trailers across red outback desert"></div>
</section>

<section class="card card-back">
  <div class="truck-photo" role="img" aria-label="Photo of a black prime mover truck with a chrome bull bar"></div>
  <div class="brand-name">WRT</div>
  <div class="contact">
    <div class="person-name">DANIEL REEVE</div>
    <div>Director</div>
    <div class="company">WRT Pty Ltd</div>
    <div>Lot 12, Banksia Road</div>
    <div>Coober Flats, Australia</div>
    <div class="lines">
      <div class="line">000 555 000
        <svg viewBox="0 0 16 16"><path d="M3 1.5l3 3-1.6 1.8c.9 2 2.3 3.4 4.3 4.3L10.5 9l3 3-2 2.5C6 14 2 10 1.5 3.5z" fill="var(--amber)"/></svg>
      </div>
      <div class="line">info@wrtservices.com.au
        <svg viewBox="0 0 16 16"><rect x="1" y="3" width="14" height="10" fill="var(--amber)"/><path d="M1 3l7 6 7-6" stroke="#0d0d0e" stroke-width="1.3" fill="none"/></svg>
      </div>
      <div class="line">wrtservices.com.au
        <svg viewBox="0 0 16 16"><circle cx="8" cy="8" r="7" fill="var(--amber)"/><path d="M1 8h14M8 1c-3 4-3 10 0 14M8 1c3 4 3 10 0 14" stroke="#0d0d0e" stroke-width="1" fill="none"/></svg>
      </div>
    </div>
  </div>
</section>

</body>
</html>
```